New business card for UK roofing company

We are Brindmore Roofing and we need a business card design for our staff.

We offer the following services:

- New roofs
- General roof repairs
- Drone surveys
- Single ply roofing
- Steel cladding
- Asbestos removal
- Electronic leak detection

I have attached our logo. I have also attached example branding printed to our vans. The business card should fit in with the style of our branding.

The business card should have the following information;

Address:
Unit 17c Wendlecroft Farm
Wendlecroft Lane
Hatchington
CM4 9QD

Telephone: 020 7946 0372
24 Hour: 0800 612 4479

Email: ray@brindmoreroofing.example
Mobile: 07700981234
Name: Ray Tunstead
Website: www.brindmoreroofing.example

The business card will be printed in Spot UV, see here: https://www.kestaprint.example/business-cards/spot-uv/

If you need anymore info, please let me know,

```html
<!DOCTYPE html>
<html lang="en">
<head>
<meta charset="utf-8">
<title>Brindmore Roofing – Business Card</title>
<link rel="stylesheet" href="https://fonts.googleapis.com/css2?family=Outfit:wght@400;500;700&display=swap">
<style>
  :root {
    --navy: #003da5;
    --cyan: #3ee0ea;
    --paper: #ffffff;
    --backdrop: #d9d9d9;
  }
  * { box-sizing: border-box; margin: 0; padding: 0; }
  html, body {
    width: 1200px; height: 846px; overflow: hidden;
    background: var(--backdrop);
    font-family: "Outfit", sans-serif;
  }
  .card {
    position: absolute; left: 346px; width: 508px; height: 290px;
    border-radius: 30px;
  }
  .card--front { top: 99px; background: var(--paper); }
  .card--back  { top: 456px; background: var(--navy); }

  .front__brand {
    position: absolute; left: 54px; top: 52px;
    display: flex; align-items: center; gap: 8px;
    font-size: 22px; font-weight: 700; color: var(--navy);
    letter-spacing: -0.5px;
  }
  .front__brand-dot {
    width: 22px; height: 22px; border-radius: 50%; background: var(--cyan);
  }
  .front__name {
    position: absolute; left: 54px; top: 128px;
    font-size: 19px; font-weight: 700; color: var(--navy);
  }
  .front__name span { color: var(--cyan); }

  .contact {
    position: absolute; left: 54px; top: 164px;
    display: flex; gap: 14px; align-items: flex-end;
    font-size: 12.5px; line-height: 17px; color: var(--navy);
  }
  .contact b { color: var(--cyan); font-weight: 700; }

  .front__rule {
    position: absolute; left: 54px; right: 54px; top: 229px;
    height: 1px; background: var(--cyan);
  }
  .front__address {
    position: absolute; left: 54px; top: 240px;
    font-size: 13.5px; color: var(--navy);
  }

  .back__mark {
    position: absolute; left: 50%; top: 62px; transform: translateX(-50%);
  }
  .back__name {
    position: absolute; left: 0; right: 0; top: 152px;
    text-align: center;
    font-size: 46px; font-weight: 700; color: var(--cyan);
    letter-spacing: -1px;
  }
</style>
</head>
<body>
  <section class="card card--front">
    <div class="front__brand">
      <span class="front__brand-dot"></span>
      <span>Brindmore Roofing</span>
    </div>
    <h1 class="front__name">Ray <span>Tunstead</span></h1>
    <div class="contact">
      <div class="contact__phones">
        <p><b>Mobile:</b> 077 0098 1234</p>
        <p><b>Telephone:</b> 020 7946 0372</p>
        <p><b>24 Hour:</b> 0800 612 4479</p>
      </div>
      <div class="contact__online">
        <p><b>Email:</b> ray@brindmoreroofing.example</p>
        <p><b>Website:</b> www.brindmoreroofing.example</p>
      </div>
    </div>
    <div class="front__rule"></div>
    <p class="front__address">Unit 17c Wendlecroft Farm, Wendlecroft Lane, Hatchington CM4 9QD</p>
  </section>

  <section class="card card--back">
    <svg class="back__mark" width="76" height="76" viewBox="0 0 76 76" aria-hidden="true">
      <circle cx="38" cy="38" r="36" fill="var(--cyan)"/>
    </svg>
    <p class="back__name">Brindmore Roofing</p>
  </section>
</body>
</html>
```